E-commerce Website Trevalin.com

Work Required
Homepage: Creation of an attractive design, clearly presenting product categories (recovery mixes, detox, etc., herbal candies).
Product Page: Highlight products with detailed information, use of mockups to represent the products.
Logo: Design a logo representative of Trevalin.com, naturally evoking the equestrian field and the organic aspect of the products.

Target Market(s)

show pdf in documents

Industry/Entity Type

show pdf in documents

Coding

Coded - Design and coding required

Requirements
Must have
• show pdf in documents
Nice to have
• show pdf in documents
Should not have
• show pdf in documents

```html
<!DOCTYPE html>
<html lang="en">
<head>
<meta charset="utf-8">
<title>Trevalin – Natural care for horses</title>
<link href="https://fonts.googleapis.com/css2?family=Poppins:wght@400;500;600;700&display=swap" rel="stylesheet">
<style>
:root{
  --canvas:#f4f2ee;
  --brown:#6e3b15;
  --brown-mid:#7b4620;
  --brown-title:#8a4b1e;
  --dark:#382312;
  --dark-foot:#3e2715;
  --olive:#5f6b2b;
  --lime:#b6cf4a;
  --tan:#d9ccb8;
  --beige:#ebe5da;
  --line:#e3ddd3;
  --text:#2f2a25;
  --muted:#8c857c;
  --cream:#efe6d6;
  --white:#fff;
}
*{box-sizing:border-box;margin:0;padding:0}
html,body{width:1200px;height:4040px;overflow:hidden}
body{background:var(--canvas);font-family:"Poppins",sans-serif;color:var(--text);font-size:11px}
.page{position:absolute;left:50px;top:350px;width:1100px;background:var(--white);box-shadow:0 4px 30px rgba(0,0,0,.06)}
.container{width:825px;margin:0 auto;position:relative}
.section-title{font-weight:600;font-size:21px;color:var(--brown-title);text-align:center;letter-spacing:.3px}
.pill{display:inline-block;border-radius:20px;padding:6px 24px;font-size:9px;font-weight:500;letter-spacing:.5px}
.pill-tan{background:var(--tan);color:var(--brown)}
.pill-olive{background:var(--olive);color:#fff}
.center{text-align:center}

.topbar{height:25px;background:var(--brown);color:#f3e7d6;font-size:8px;display:flex;align-items:center;justify-content:space-between;padding:0 137px}
.topbar em{font-style:normal;color:var(--lime)}
.lang{display:flex;background:#c9b79e;border-radius:10px;padding:2px;gap:2px}
.lang span{padding:1px 7px;border-radius:8px;font-size:7px;color:var(--brown)}
.lang .on{background:#fff}

.header{height:88px;display:flex;align-items:center;padding:0 137px}
.brand{display:flex;align-items:center;gap:8px;font-weight:700;font-size:24px;color:var(--brown)}
.brand i{width:30px;height:30px;border-radius:50%;background:var(--olive);display:block}
.nav{display:flex;gap:24px;margin-left:108px;font-size:10px;color:var(--text)}
.nav .active{color:var(--brown-mid);text-decoration:underline}
.tools{margin-left:auto;display:flex;gap:8px;align-items:center}
.search{width:128px;height:28px;border:1px solid var(--line);border-radius:16px;display:flex;align-items:center;justify-content:space-between;padding:0 10px;color:var(--muted);font-size:9px}
.round{width:28px;height:28px;border:1px solid var(--line);border-radius:50%;display:flex;align-items:center;justify-content:center}
.cart{height:28px;border:1px solid var(--line);border-radius:16px;padding:0 10px;display:flex;align-items:center;gap:5px;font-weight:600;font-size:10px}

.hero{height:418px;position:relative;background:linear-gradient(90deg,#3b2412 0%,#6a4220 45%,#9a6a3c 70%,#5a3619 100%)}
.hero-copy{position:absolute;left:152px;top:140px;width:310px;text-align:center;color:#fff}
.hero-copy h1{font-size:22px;font-weight:500;line-height:1.36;letter-spacing:.3px}
.hero-copy .pill{background:var(--tan);color:var(--brown);margin-top:22px;padding:8px 22px}

.features{height:88px;background:var(--brown-mid);display:flex;align-items:center;padding:0 40px}
.feature{flex:1;display:flex;gap:10px;align-items:center;padding:0 10px;border-right:1px solid rgba(255,255,255,.18);color:#f1e4d2;font-size:7.5px;line-height:1.35}
.feature:last-child{border:0}
.feature b{display:block;color:#e6c89a;font-weight:500;font-size:9px}
.feature svg{flex:none}

.categories{height:399px;padding-top:66px}
.cat-row{display:flex;gap:20px;margin-top:26px}
.cat{width:121px;height:165px;border:1px solid var(--line);border-radius:6px;padding:3px;text-align:center;font-size:9px;line-height:1.35}
.cat .ph{height:110px;border-radius:4px;margin-bottom:10px}
.cat.hover{color:var(--olive);text-decoration:underline}

.deals{height:474px;background:var(--beige);padding-top:64px}
.deal-row{display:flex;gap:24px;margin-top:24px}
.deal{width:188px;text-align:center;font-size:9.5px}
.deal .box{height:184px;background:#fff;border-radius:8px;position:relative;display:flex;align-items:center;justify-content:center}
.badge{position:absolute;top:7px;right:7px;border-radius:6px;color:#fff;font-size:7px;padding:2px 6px}
.tub{width:104px;height:130px;border-radius:6px 6px 14px 14px;background:linear-gradient(#f2f2f2,#dcdcdc)}
.tub .lbl{width:52px;height:52px;margin:38px auto 0;border-radius:4px;background:linear-gradient(135deg,#9fc7c9,#6e9a4f)}
.deal h4{font-weight:400;margin-top:12px;line-height:1.4}
.price{margin-top:6px}
.price s{color:#c89c78;margin-left:8px}
.qv{position:absolute;left:76px;top:72px;width:36px;height:36px;border-radius:50%;background:var(--olive);display:flex;align-items:center;justify-content:center}

.blog{height:515px;padding-top:66px}
.blog-row{display:flex;gap:24px;margin-top:26px}
.post{width:259px;height:283px;border:1px solid var(--line);border-radius:6px;padding:3px}
.post .ph{height:160px;border-radius:4px}
.post .body{padding:14px 12px}
.post .date{font-size:8px;color:var(--text);display:flex;gap:6px;align-items:center}
.post h4{font-size:10.5px;font-weight:600;line-height:1.4;margin:7px 0 9px}
.post a{font-size:8px;color:#c89c78;text-decoration:underline}

.horses{height:682px;background:var(--dark);padding-top:72px}
.horses .section-title{color:#b97a44}
.hgrid{display:flex;flex-wrap:wrap;gap:22px 22px;margin-top:18px}
.hcard{height:239px;position:relative;border-radius:4px}
.hcard span{position:absolute;left:0;bottom:0;background:var(--cream);padding:9px 22px 7px 20px;border-radius:0 12px 0 4px;font-size:14px;font-weight:500;color:var(--dark)}

.news{height:319px;display:flex;align-items:center;padding-left:255px}
.news .art{width:195px;height:185px;border-radius:8px;background:linear-gradient(135deg,#f3d48a,#e8b75b 60%,#6b4a2a)}
.news-form{margin-left:45px}
.news-form small{font-size:12px;color:var(--brown-title)}
.news-form h3{font-size:21px;font-weight:600;color:var(--brown-title);margin-bottom:14px}
.fields{display:grid;grid-template-columns:170px 170px;gap:8px 10px}
.field{height:28px;border:1px solid var(--line);border-radius:14px;padding:0 14px;display:flex;align-items:center;font-size:8px;color:var(--muted)}
.field.tall{grid-row:span 2;height:64px;align-items:flex-start;padding-top:8px;border-radius:10px}
.news-form .pill{margin-top:18px}

.footer{height:330px;background:var(--dark-foot);color:#e9dccb;font-size:9px;line-height:1.7;position:relative}
.fcols{display:flex;padding-top:54px}
.fcols h5{color:#c58549;font-size:12px;font-weight:500;margin-bottom:8px}
.fabout{width:242px;padding-top:10px}
.fabout .brand{color:#e5c79a;margin-bottom:24px}
.fabout .brand i{background:#9b6a3a}
.fabout p{margin-bottom:10px;line-height:1.45}
.fabout a{color:#c89c78;text-decoration:underline}
.fcontact{width:207px}
.row{display:flex;gap:8px;margin-bottom:8px;line-height:1.45}
.row svg{flex:none;margin-top:2px}
.row.big{font-size:12px}
.fcat{width:137px}
.fcat .on{color:#c89c78;text-decoration:underline}
.fhelp{width:124px}
.social{display:flex;gap:8px;margin-top:4px}
.social i{width:26px;height:26px;border-radius:50%;border:1px solid #7d6148;display:block}
.social i.on{background:var(--olive);border-color:var(--olive)}
.fbottom{position:absolute;left:137px;right:137px;bottom:26px;display:flex;justify-content:space-between;align-items:center;font-size:8.5px}
.cards{display:flex;gap:6px}
.cards i{width:22px;height:22px;border-radius:50%;background:#e7e1d6;display:block}
</style>
</head>
<body>
<div class="page">

  <div class="topbar">
    <div>Because their well-being is your priority - <em>100% Made in France</em></div>
    <div class="lang"><span class="on">EN</span><span>FR</span></div>
  </div>

  <header class="header">
    <div class="brand"><i></i>Trevalin</div>
    <nav class="nav">
      <span class="active">Home</span><span>Categories</span><span>About us</span><span>Our stores</span><span>Blog</span>
    </nav>
    <div class="tools">
      <div class="search">Search
        <svg width="11" height="11" viewBox="0 0 12 12" fill="none" stroke="#333" stroke-width="1.3"><circle cx="5" cy="5" r="3.8"/><path d="M8 8l3 3"/></svg>
      </div>
      <div class="round"><svg width="12" height="12" viewBox="0 0 12 12" fill="none" stroke="#333" stroke-width="1.2"><circle cx="6" cy="4" r="2.4"/><path d="M1.5 11c.8-2.6 2.5-3.6 4.5-3.6s3.7 1 4.5 3.6"/></svg></div>
      <div class="cart"><svg width="12" height="12" viewBox="0 0 12 12" fill="none" stroke="#333" stroke-width="1.2"><path d="M1 1.5h2l1.3 6h5.4L11 3.5H3.5"/><circle cx="5" cy="10" r=".8"/><circle cx="9" cy="10" r=".8"/></svg>$ 0.00</div>
    </div>
  </header>

  <section class="hero" role="img" aria-label="Hands scooping grain horse feed from a burlap sack in warm light">
    <div class="hero-copy">
      <h1>YOUR NATURAL ALLY FOR THE HEALTH AND WELL-BEING OF YOUR</h1>
      <span class="pill">SHOP NOW</span>
    </div>
  </section>

  <section class="features">
    <div class="feature"><svg width="36" height="36" viewBox="0 0 36 36" fill="none" stroke="#e6c89a" stroke-width="1.3"><rect x="3" y="12" width="18" height="12"/><path d="M21 16h7l4 5v3H21"/><circle cx="9" cy="27" r="3"/><circle cx="27" cy="27" r="3"/></svg><div><b>DELIVERY</b>Free shipping from 65 € HT of purchase (France)</div></div>
    <div class="feature"><svg width="36" height="36" viewBox="0 0 36 36" fill="none" stroke="#e6c89a" stroke-width="1.3"><rect x="5" y="9" width="26" height="18" rx="2"/><path d="M13 23l10-10"/><circle cx="13" cy="14" r="2"/><circle cx="23" cy="22" r="2"/></svg><div><b>LOYALTY</b>Rewarded 5%, 10%, 15% in vouchers*</div></div>
    <div class="feature"><svg width="36" height="36" viewBox="0 0 36 36" fill="none" stroke="#e6c89a" stroke-width="1.3"><circle cx="18" cy="12" r="5"/><path d="M8 31c1-6 5-9 10-9s9 3 10 9"/></svg><div>Professional and personalized<b>NUTRITION ADVICE</b>on 01 23 45 67 80</div></div>
    <div class="feature"><svg width="36" height="36" viewBox="0 0 36 36" fill="none" stroke="#e6c89a" stroke-width="1.3"><rect x="6" y="16" width="24" height="14"/><path d="M6 16l4-7h16l4 7M14 16v14M22 16v14"/></svg><div><b>GROUPING</b>Combine your food orders with other customers</div></div>
    <div class="feature"><svg width="36" height="36" viewBox="0 0 36 36" fill="none" stroke="#e6c89a" stroke-width="1.3"><path d="M18 30s-8-8-8-14a8 8 0 0116 0c0 6-8 14-8 14z"/><circle cx="18" cy="16" r="3"/></svg><div><b>FIND A STORE</b>Find a store near you</div></div>
    <div class="feature"><svg width="36" height="36" viewBox="0 0 36 36" fill="none" stroke="#e6c89a" stroke-width="1.3"><path d="M18 5l11 4v8c0 7-5 12-11 14-6-2-11-7-11-14V9z"/><path d="M13 18l4 4 6-7"/></svg><div><b>SECURITY</b>For your payments by card or transfer</div></div>
  </section>

  <section class="categories">
    <div class="container">
      <h2 class="section-title">Shop by Category</h2>
      <div class="cat-row">
        <div class="cat"><div class="ph" role="img" aria-label="Dried herbs in bulk" style="background:linear-gradient(135deg,#5b4a34,#a88a55)"></div>Organic<br>Herbs In Bulk</div>
        <div class="cat"><div class="ph" role="img" aria-label="Dark organic horse treats" style="background:linear-gradient(135deg,#2e2620,#6b5a48)"></div>Organic<br>Treats</div>
        <div class="cat"><div class="ph" role="img" aria-label="Golden recovery mix" style="background:linear-gradient(135deg,#8a6a2c,#c4a25a)"></div>Organic<br>Recovery Elixir</div>
        <div class="cat"><div class="ph" role="img" aria-label="Green dried herb blend" style="background:linear-gradient(135deg,#6e6a3a,#a9a56a)"></div>Organic<br>Digesti-Boost</div>
        <div class="cat hover"><div class="ph" role="img" aria-label="Green feed pellets" style="background:linear-gradient(135deg,#2f3a24,#5e6b44)"></div>Organic<br>Equine Detox</div>
        <div class="cat"><div class="ph" role="img" aria-label="Fresh green herb shoots" style="background:linear-gradient(135deg,#6f8e3e,#b8c79a)"></div>Organic<br>Balance (Stress)</div>
      </div>
      <div class="center" style="margin-top:32px"><span class="pill pill-tan">VIEW ALL</span></div>
    </div>
  </section>

  <section class="deals">
    <div class="container">
      <h2 class="section-title">Hot Deals</h2>
      <div class="deal-row">
        <div class="deal"><div class="box"><span class="badge" style="background:#d0553a">-17%</span><div class="tub" role="img" aria-label="Tub of aromatic herb treats"><div class="lbl"></div></div></div><h4>Sweet Organic Aromatic<br>Herbs</h4><div class="price">€26.00<s>€35.00</s></div></div>
        <div class="deal"><div class="box"><span class="badge" style="background:#e0a85a">Best Seller</span><div class="tub" role="img" aria-label="Tub of aromatic herb treats"><div class="lbl"></div></div></div><h4>Sweet Organic Aromatic<br>Herbs</h4><div class="price">€26.00<s>€35.00</s></div></div>
        <div class="deal"><div class="box"><span class="badge" style="background:#d86a55">Sold Out</span><div class="tub" role="img" aria-label="Tub of aromatic herb treats"><div class="lbl"></div></div></div><h4>Sweet Organic Aromatic<br>Herbs</h4><div class="price">€26.00<s>€35.00</s></div></div>
        <div class="deal"><div class="box"><span class="badge" style="background:var(--olive)">New</span><div class="tub" role="img" aria-label="Tub of aromatic herb treats" style="opacity:.55"><div class="lbl"></div></div><div class="qv"><svg width="14" height="14" viewBox="0 0 12 12" fill="none" stroke="#fff" stroke-width="1.2"><path d="M1 1.5h2l1.3 6h5.4L11 3.5H3.5"/><circle cx="5" cy="10" r=".8"/><circle cx="9" cy="10" r=".8"/></svg></div></div><h4>Sweet Organic Aromatic<br>Herbs</h4><div class="price">€26.00<s>€35.00</s></div></div>
      </div>
      <div class="center" style="margin-top:30px"><span class="pill pill-olive">VIEW ALL</span></div>
    </div>
  </section>

  <section class="blog">
    <div class="container">
      <h2 class="section-title">Our Blog</h2>
      <div class="blog-row">
        <article class="post"><div class="ph" role="img" aria-label="Rider feeding a horse at a paddock fence" style="background:linear-gradient(135deg,#6d8a4a,#c7a06a 60%,#5a3c22)"></div><div class="body"><div class="date"><svg width="10" height="10" viewBox="0 0 10 10" fill="none" stroke="#8a4b1e"><rect x="1" y="2" width="8" height="7"/><path d="M1 4h8M3 1v2M7 1v2"/></svg>Fab 01, 2024</div><h4>Lorem Ipsum is simply dummy text of the printing and typesetting industry.</h4><a>Read More</a></div></article>
        <article class="post"><div class="ph" role="img" aria-label="Loose dried herbs on linen" style="background:linear-gradient(135deg,#2a2520,#5c5448 50%,#d8d0c2)"></div><div class="body"><div class="date"><svg width="10" height="10" viewBox="0 0 10 10" fill="none" stroke="#8a4b1e"><rect x="1" y="2" width="8" height="7"/><path d="M1 4h8M3 1v2M7 1v2"/></svg>Fab 01, 2024</div><h4>Lorem Ipsum is simply dummy text of the printing and typesetting industry.</h4><a>Read More</a></div></article>
        <article class="post"><div class="ph" role="img" aria-label="Rider standing beside a bay horse in autumn" style="background:linear-gradient(135deg,#c79a3a,#e8e2d6 50%,#4a2c18)"></div><div class="body"><div class="date"><svg width="10" height="10" viewBox="0 0 10 10" fill="none" stroke="#8a4b1e"><rect x="1" y="2" width="8" height="7"/><path d="M1 4h8M3 1v2M7 1v2"/></svg>Fab 01, 2024</div><h4>Lorem Ipsum is simply dummy text of the printing and typesetting industry.</h4><a>Read More</a></div></article>
      </div>
      <div class="center" style="margin-top:32px"><span class="pill pill-tan">VIEW ALL</span></div>
    </div>
  </section>

  <section class="horses">
    <div class="container">
      <h2 class="section-title">Verdane for Each Horse</h2>
      <div class="hgrid">
        <div class="hcard" style="width:476px;background:linear-gradient(135deg,#8aa06a,#b07a48 55%,#6f8a4a)" role="img" aria-label="Mare and foal grazing in a meadow"><span>Breeding</span></div>
        <div class="hcard" style="width:327px;background:linear-gradient(135deg,#8b9096,#5a4a3c 60%,#9a9ea2)" role="img" aria-label="Harness racing horse on a track"><span>Racing Horse</span></div>
        <div class="hcard" style="width:228px;background:linear-gradient(135deg,#9ab36a,#3a2a20 60%,#6d8a3e)" role="img" aria-label="Rider with a dark horse outdoors"><span>Leisure Horse</span></div>
        <div class="hcard" style="width:325px;background:linear-gradient(180deg,#c5c9cc,#6a6c6a 60%,#4c4034)" role="img" aria-label="Show jumper clearing a fence"><span>Sport Horse</span></div>
        <div class="hcard" style="width:228px;background:linear-gradient(135deg,#8aa85a,#e3e1dc 50%,#9a7a5a)" role="img" aria-label="Woman with a grey senior horse"><span>Senior Horse</span></div>
      </div>
    </div>
  </section>

  <section class="news">
    <div class="art" role="img" aria-label="Illustration of an envelope with a letter and paper plane"></div>
    <div class="news-form">
      <small>Sign up for</small>
      <h3>Our latest offerings!</h3>
      <div class="fields">
        <div class="field">Your Name</div>
        <div class="field tall">Message</div>
        <div class="field">Your Email</div>
      </div>
      <span class="pill pill-tan">SUBSCRIBE</span>
    </div>
  </section>

  <footer class="footer">
    <div class="container fcols">
      <div class="fabout">
        <div class="brand"><i></i>Trevalin</div>
        <p>Discover our passion for sport horses and animal welfare</p>
        <p>Passionate about horse riding and with several years of practice, we decided to create <a>Read More</a></p>
      </div>
      <div class="fcontact">
        <h5>Contact Us</h5>
        <div class="row big"><svg width="11" height="11" viewBox="0 0 12 12" fill="none" stroke="#c58549" stroke-width="1.2"><path d="M2 1h3l1 3-2 1a7 7 0 003 3l1-2 3 1v3c-5 1-10-4-9-9z"/></svg>01 23 45 67 89</div>
        <div class="row"><svg width="11" height="11" viewBox="0 0 12 12" fill="none" stroke="#c58549" stroke-width="1.2"><rect x="1" y="2.5" width="10" height="7"/><path d="M1 3l5 4 5-4"/></svg>hello@trevalin.com</div>
        <div class="row"><svg width="11" height="11" viewBox="0 0 12 12" fill="none" stroke="#c58549" stroke-width="1.2"><path d="M6 11S2 7 2 4.5a4 4 0 018 0C10 7 6 11 6 11z"/><circle cx="6" cy="4.5" r="1.3"/></svg>27 Orchard Lane,<br>Brookvale 4120,<br>Valmont</div>
        <div class="row"><svg width="11" height="11" viewBox="0 0 12 12" fill="none" stroke="#c58549" stroke-width="1.2"><circle cx="6" cy="6" r="5"/><path d="M6 3v3l2 1"/></svg>Mon - Sat: 10 AM &nbsp;to 7 PM<br>Sun: close</div>
      </div>
      <div class="fcat">
        <h5>Categories</h5>
        <div class="on">Home</div><div>Categories</div><div>About us</div><div>Our stores</div><div>Blog</div>
        <h5 style="margin-top:10px">Follow us</h5>
        <div class="social"><i></i><i></i><i class="on"></i><i></i><i></i><i></i></div>
      </div>
      <div class="fhelp">
        <h5>Help</h5>
        <div>Payments</div><div>Shipping</div><div>Cancellation</div><div>FAQ</div><div>Report</div>
      </div>
      <div>
        <h5>Policy</h5>
        <div>Return Policy</div><div>Terms Of Use</div><div>Security</div><div>Privacy</div><div>Sitemap</div>
      </div>
    </div>
    <div class="fbottom">
      <div>© 2024 Trevalin. All Right Reserved</div>
      <div class="cards"><i></i><i></i><i></i><i></i><i></i></div>
    </div>
  </footer>

</div>
</body>
</html>
```